Expense Tracker App for Young Adults

I need a mobile app designer to design an app UI for me. It is for an expense tracker app. I’ve attached a mind map of the various screens and features of the app.

I would like to see designs for this app which is targeted towards young adults (late teens & early 20s) just starting their career who want to plan their budgets and track their expenses.
Updates

Hello designers! I'm conscious that this is not a guaranteed project, so I can understand that some of you might be apprehensive. Just wanted to let you know that I'm willing to see your initial drafts that show your direction and theme for design. You don't have to design the whole app. In fact, it's better if you share your initial design ideas so that we can have a discussion and I can give my input. If I see some good initial designs, I will be happy to make this a guaranteed project. I'm simply being cautious since I'm bootstrapping this and funding out of my own pocket. Thank you for your understanding!

Target Market(s)

Young adults who are just starting their careers, late teens and early 20s.

Font styles to use
Sans Serif

Requirements
Must have
• Ease of use, smart and sleek, a guided setup wizard which will help users setup their account after signing up.
Should not have
• Clunky

```html
<!DOCTYPE html>
<html lang="en">
<head>
<meta charset="utf-8">
<title>KOA Expense Tracker – Screens</title>
<link rel="stylesheet" href="https://fonts.googleapis.com/css2?family=Fira+Sans:wght@400;500;600;700&display=swap">
<style>
  :root {
    --canvas-bg: #d3d4d6;
    --screen-blue: #2d6fb5;
    --screen-blue-light: #3a7fc4;
    --screen-blue-dark: #265f9f;
    --header-bg: #ffffff;
    --brand-blue: #2d6fb5;
    --ink: #111111;
    --white: #ffffff;
    --accent: #f6a81f;
    --track: #4a8fd6;
  }
  * { box-sizing: border-box; margin: 0; padding: 0; }
  html, body { width: 1200px; height: 719px; overflow: hidden; }
  body {
    background: var(--canvas-bg);
    font-family: "Fira Sans", Arial, sans-serif;
    position: relative;
    color: var(--white);
  }
  .screen {
    position: absolute;
    top: 76px;
    width: 311px;
    height: 554px;
  }
  .screen--settings { left: 75px; }
  .screen--expenses { left: 433px; }
  .screen--reports  { left: 793px; }

  .app-header {
    height: 50px;
    background: var(--header-bg);
    display: flex;
    align-items: center;
    justify-content: space-between;
    padding: 0 18px 0 21px;
  }
  .app-name { color: var(--brand-blue); font-weight: 600; font-size: 15px; letter-spacing: .3px; }
  .screen-title { color: var(--ink); font-weight: 500; font-size: 15px; letter-spacing: .3px; }

  .screen-body {
    position: relative;
    height: 504px;
    background:
      radial-gradient(ellipse at 30% 20%, rgba(255,255,255,.06), transparent 60%),
      radial-gradient(ellipse at 80% 75%, rgba(255,255,255,.05), transparent 55%),
      linear-gradient(160deg, var(--screen-blue-light), var(--screen-blue) 50%, var(--screen-blue-dark));
  }

  .outline-button {
    position: absolute;
    left: 23px;
    width: 268px;
    border: 2px solid var(--white);
    display: flex;
    align-items: center;
    font-weight: 600;
    font-size: 15px;
    letter-spacing: .3px;
    color: var(--white);
  }
  .outline-button .icon { width: 18px; margin: 0 14px 0 19px; display: flex; justify-content: center; }
  .outline-button .chevron { margin-left: auto; margin-right: 18px; display: flex; }
  .outline-button--stacked { line-height: 20px; }

  .btn-notifications { top: 87px; height: 63px; }
  .btn-currency { top: 173px; height: 55px; }
  .btn-language { top: 255px; height: 55px; }
  .btn-logout {
    position: absolute; left: 23px; top: 339px; width: 268px; height: 55px;
    background: var(--accent);
    display: flex; align-items: center; justify-content: center;
    font-weight: 700; font-size: 21px; letter-spacing: .5px;
    box-shadow: 0 2px 4px rgba(0,0,0,.15);
  }

  .field-label {
    position: absolute; left: 23px;
    font-weight: 500; font-size: 15px; letter-spacing: .2px;
  }
  .field-label small { font-size: 12.5px; }
  .label-sort { top: 42px; }
  .label-category { top: 155px; }
  .label-start { top: 262px; }
  .label-end { top: 367px; }

  .range-slider { position: absolute; left: 23px; top: 78px; width: 268px; height: 18px; }
  .range-labels { position: absolute; top: 102px; left: 23px; width: 268px; font-size: 10px; }
  .range-labels span { position: absolute; }
  .range-labels .min { left: 0; }
  .range-labels .max { left: 90px; }

  .input-box {
    position: absolute; left: 24px; width: 274px; height: 45px;
    border: 2px solid var(--white);
    display: flex; align-items: center; justify-content: space-between;
    padding: 0 16px 0 17px;
    font-size: 13.5px;
  }
  .input-select { top: 190px; font-weight: 500; font-size: 13px; }
  .input-start { top: 297px; }
  .input-end { top: 405px; }

  .btn-goals { top: 153px; height: 52px; justify-content: center; }
  .btn-history { top: 225px; height: 52px; justify-content: center; }
  .btn-history .chevron { margin: 0 0 0 10px; }
</style>
</head>
<body>

  <section class="screen screen--settings">
    <header class="app-header"><span class="app-name">KOA</span><span class="screen-title">SETTINGS</span></header>
    <div class="screen-body" role="img" aria-label="Blue background with soft flowing light lines">
      <div class="outline-button outline-button--stacked btn-notifications">
        <span class="icon"><svg width="18" height="18" viewBox="0 0 18 18"><path d="M9 1.5a1.2 1.2 0 0 1 1.2 1.2v.6A5 5 0 0 1 14 8.2v3.6l1.8 2.2H2.2L4 11.8V8.2a5 5 0 0 1 3.8-4.9v-.6A1.2 1.2 0 0 1 9 1.5zM7 15h4a2 2 0 0 1-4 0z" fill="#fff"/></svg></span>
        <span>NOTIFICATION<br>PREFERENCES</span>
        <span class="chevron"><svg width="12" height="20" viewBox="0 0 12 20"><path d="M2 2l8 8-8 8" stroke="#fff" stroke-width="2.4" fill="none"/></svg></span>
      </div>
      <div class="outline-button btn-currency">
        <span class="icon"><svg width="14" height="22" viewBox="0 0 14 22"><path d="M7 1v20M11.5 5.5C10.5 4 9 3.5 7 3.5 4.5 3.5 2.5 4.8 2.5 7s2 3 4.5 3.6 4.8 1.5 4.8 3.9S9.5 18.5 7 18.5c-2.2 0-4-.8-5-2.4" stroke="#fff" stroke-width="2.2" fill="none"/></svg></span>
        <span>CURRENCY</span>
      </div>
      <div class="outline-button btn-language">
        <span class="icon"><svg width="17" height="17" viewBox="0 0 17 17"><circle cx="8.5" cy="8.5" r="8" fill="#fff"/><path d="M4 4.5c1.5.5 2 1.5 1.5 3s1 2 1 3.5M10 2c-.5 1.5 1 2 2.5 2.5M11 9.5c1.5 0 2.5 1 2 3" stroke="#2d6fb5" stroke-width="1.6" fill="none"/></svg></span>
        <span>LANGUAGE</span>
      </div>
      <div class="btn-logout">LOGOUT</div>
    </div>
  </section>

  <section class="screen screen--expenses">
    <header class="app-header"><span class="app-name">KOA</span><span class="screen-title">VIEW EXPENSES</span></header>
    <div class="screen-body" role="img" aria-label="Blue background with soft flowing light lines">
      <div class="field-label label-sort">SORT BY AMOUNT</div>
      <svg class="range-slider" viewBox="0 0 268 18">
        <rect x="0" y="6.5" width="268" height="5" fill="var(--track)"/>
        <rect x="7" y="6.5" width="94" height="5" fill="var(--accent)"/>
        <circle cx="8" cy="9" r="8.5" fill="var(--accent)"/>
        <circle cx="101" cy="9" r="8.5" fill="var(--accent)"/>
      </svg>
      <div class="range-labels"><span class="min">$0</span><span class="max">$100</span></div>

      <div class="field-label label-category">FILTER BY CATEGORY</div>
      <div class="input-box input-select">
        <span>SELECT</span>
        <svg width="14" height="8" viewBox="0 0 14 8"><path d="M0 0h14L7 8z" fill="#fff"/></svg>
      </div>

      <div class="field-label label-start">FILTER BY <small>(START DATE )</small></div>
      <div class="input-box input-start">
        <span>dd/mm/yyyy</span>
        <svg width="12" height="12" viewBox="0 0 12 12"><rect x="1" y="2" width="10" height="9" fill="none" stroke="#fff" stroke-width="1.2"/><path d="M1 4.5h10M3.5 0.5v2.5M8.5 0.5v2.5" stroke="#fff" stroke-width="1.2"/></svg>
      </div>

      <div class="field-label label-end">FILTER BY <small>(END DATE )</small></div>
      <div class="input-box input-end">
        <span>dd/mm/yyyy</span>
        <svg width="12" height="12" viewBox="0 0 12 12"><rect x="1" y="2" width="10" height="9" fill="none" stroke="#fff" stroke-width="1.2"/><path d="M1 4.5h10M3.5 0.5v2.5M8.5 0.5v2.5" stroke="#fff" stroke-width="1.2"/></svg>
      </div>
    </div>
  </section>

  <section class="screen screen--reports">
    <header class="app-header"><span class="app-name">KOA</span><span class="screen-title">VIEW REPORTS</span></header>
    <div class="screen-body" role="img" aria-label="Blue background with soft flowing light lines">
      <div class="outline-button btn-goals">PROGRESS AGAINST GOALS</div>
      <div class="outline-button btn-history">HISTORICAL EXPENSES
        <span class="chevron"><svg width="10" height="18" viewBox="0 0 10 18"><path d="M1.5 1.5l7 7.5-7 7.5" stroke="#fff" stroke-width="2.2" fill="none"/></svg></span>
      </div>
    </div>
  </section>

</body>
</html>
```